Ironvale Shift Services

We are a underground coal mining labour hire company, needing a website that links into our online payroll (www.wagetrakker.com.au) and also need to have job applications page that is a preform with drop down menu,s with answers or check boxes. We would also need a 3 tier administration access for access to different files.
We are looking for an ongoing relationship with future app integration

Reason: There are a few more designs to come and I'm out at the mine for another week

Industry/Entity Type

Coal Mining

```html
<!DOCTYPE html>
<html lang="en">
<head>
<meta charset="utf-8">
<title>Ironvale Shift Services</title>
<link href="https://fonts.googleapis.com/css2?family=Open+Sans:wght@400;600;700&display=swap" rel="stylesheet">
<style>
:root{
  --orange:#f06a1a;
  --header:#140c06;
  --footer-dark:#0b0705;
  --panel:#f2f0f0;
  --text:#3a3a3a;
  --heading:#1c1c1c;
  --rule:#dcdcdc;
  --white:#ffffff;
}
*{margin:0;padding:0;box-sizing:border-box}
html,body{width:986px;height:1200px;overflow:hidden;background:var(--white);font-family:"Open Sans",Arial,sans-serif;color:var(--text)}
.page{position:relative;width:986px;height:1200px}
.abs{position:absolute}

.site-header{left:0;top:0;width:986px;height:80px;background:var(--header);border-bottom:3px solid var(--orange)}
.brand{left:131px;top:2px;height:74px;display:flex;align-items:center;gap:10px}
.brand-mark{width:22px;height:22px;background:var(--orange)}
.brand-name{color:var(--white);font-size:28px;font-weight:600;letter-spacing:1px}
.main-nav{left:358px;top:32px;display:flex;font-size:10.5px;color:var(--white)}
.main-nav span{position:absolute;top:0;white-space:nowrap;line-height:20px}
.main-nav .active{background:var(--orange);padding:0 6px;left:0}

.hero{left:139px;top:105px;width:707px;height:285px;background:linear-gradient(160deg,#1d2430 0%,#3a2a22 45%,#6a4330 75%,#2a1f1a 100%)}
.hero-title{left:411px;top:24px;color:var(--white);font-size:27px;line-height:35px;font-weight:400;text-shadow:0 1px 3px rgba(0,0,0,.6)}
.hero-dots{right:21px;bottom:12px;display:flex;gap:5px}
.hero-dots i{width:7px;height:7px;border-radius:50%;background:#bbb;display:block}
.hero-dots i:first-child{background:var(--orange)}

.section-title{font-size:13px;font-weight:600;color:var(--heading)}
.section-title em{font-style:normal;font-weight:400;color:var(--orange)}
.body-text{font-size:8.6px;line-height:14px}

.welcome{left:140px;top:410px;width:706px;height:149px;background:var(--panel)}
.welcome .section-title{left:18px;top:9px}
.welcome-photo{left:17px;top:43px;width:126px;height:87px;background:linear-gradient(135deg,#2a2a30,#5a4a3a 55%,#1e1e24)}
.welcome-rule{left:170px;top:43px;width:1px;height:82px;background:#cfcfcf}
.welcome .body-text{left:188px;top:43px;width:505px}
.welcome p+p{margin-top:14px}

.services .section-title{left:154px;top:581px}
.services-intro{left:156px;top:612px;width:385px}
.service-list{left:154px;top:682px;width:370px;list-style:none}
.service-list li{position:relative;padding-left:17px;margin-bottom:6px}
.service-list svg{position:absolute;left:0;top:3px}
.services-photo{left:571px;top:613px;width:237px;height:158px;background:linear-gradient(180deg,#8a9aa8 0%,#6b5a4a 25%,#8a5a3a 60%,#c07040 100%)}
.divider{left:140px;top:808px;width:706px;height:1px;background:var(--rule)}

.news .section-title{left:154px;top:830px}
.news-item{left:154px;width:236px}
.news-date{color:var(--orange);font-size:8.6px;line-height:12px}
.news-sep{left:154px;top:927px;width:226px;border-top:1px dotted #c8c8c8}
.about .section-title{left:422px;top:830px}
.about .body-text{left:422px;top:865px;width:410px;text-align:justify}
.about p+p{margin-top:14px}
.btn{background:var(--orange);color:var(--white);font-size:9.5px;height:18px;line-height:18px;padding:0 7px;box-shadow:0 1px 2px rgba(0,0,0,.25)}

.footer-band{left:0;top:1082px;width:986px;height:39px;background:var(--orange)}
.footer-links{left:156px;top:13px;font-size:8.6px;color:var(--white)}
.social{left:710px;top:10px;display:flex;gap:6px}
.social i{width:19px;height:19px;display:block;border-radius:2px}
.footer-bottom{left:0;top:1121px;width:986px;height:79px;background:var(--footer-dark)}
.copyright{left:154px;top:34px;font-size:8.6px;color:#9a9a9a}
.copyright b{font-weight:600;color:#b5b5b5}
.payroll-brand{left:691px;top:24px;display:flex;align-items:center;gap:6px;color:#8a8a8a;font-size:24px}
.payroll-brand i{width:22px;height:22px;background:#6a6a6a;display:block}
</style>
</head>
<body>
<div class="page">

  <header class="site-header abs">
    <div class="brand abs"><span class="brand-mark"></span><span class="brand-name">ISS</span></div>
    <nav class="main-nav abs">
      <span class="active">Home</span>
      <span style="left:56px">Apply for position</span>
      <span style="left:161px">Pay Portal</span>
      <span style="left:232px">Download</span>
      <span style="left:303px">Mission</span>
      <span style="left:366px">About us</span>
      <span style="left:428px">Contact us</span>
    </nav>
  </header>

  <section class="hero abs" role="img" aria-label="Coal miner with a head lamp beam over a night city skyline">
    <h1 class="hero-title abs">Ironvale Shift<br>Services</h1>
    <div class="hero-dots abs"><i></i><i></i><i></i></div>
  </section>

  <section class="welcome abs">
    <h2 class="section-title abs"><em>Welcome to</em> Ironvale Shift Services</h2>
    <div class="welcome-photo abs" role="img" aria-label="Two miners with head lamps underground"></div>
    <div class="welcome-rule abs"></div>
    <div class="body-text abs">
      <p>We are Karrow Holdings pty ltd trading as Ironvale Shift Services,&nbsp; we are experienced in ground consolidation in underground coal mines,&nbsp; in short when they collapse or cave in we come in with chemical pumps and stabilise the ground or fill cavities which will then allow for the mining process to continue. We also do general mine labor as well.</p>
      <p>We are a labor hire company for major mining services company,&nbsp; we offer labor solutions in New South Wales and Queensland in the underground coal mines.</p>
    </div>
  </section>

  <section class="services">
    <h2 class="section-title abs"><em>Our</em> Services</h2>
    <p class="services-intro body-text abs">Morbi interdum mollis sapien. Sed ac risus. Phasellus lacinia, magna a ullamcorper laoreet, lectus arcu pulvinar risus, vitae facilisis libero dolor a purus. Sed vel lacus. Mauris nibh felis, adipiscing varius, adipiscing in, lacinia vel, tellus. Suspendisse ac urna. Etiam pellentesque mauris ut lectus. Nunc tellus ante, mattis eget, gravida vitae, ultricies ac, leo. Integer leo pede</p>
    <ul class="service-list body-text abs">
      <li><svg width="8" height="9" viewBox="0 0 8 9"><path d="M1 0.5 L6.5 4.5 L1 8.5" fill="none" stroke="#f06a1a" stroke-width="2"/></svg>Morbi interdum mollis sapien. Sed ac risus. Phasellus lacinia, magna</li>
      <li><svg width="8" height="9" viewBox="0 0 8 9"><path d="M1 0.5 L6.5 4.5 L1 8.5" fill="none" stroke="#f06a1a" stroke-width="2"/></svg>ullamcorper laoreet, lectus arcu pulvinar risus, vitae facilisis libero dolor a purus. Sed vel lacus. Mauris nibh felis,</li>
      <li style="margin-bottom:11px"><svg width="8" height="9" viewBox="0 0 8 9"><path d="M1 0.5 L6.5 4.5 L1 8.5" fill="none" stroke="#f06a1a" stroke-width="2"/></svg>adipiscing varius, adipiscing in, lacinia vel, tellus. Suspendisse ac urna. Etiam pellentesque</li>
      <li><svg width="8" height="9" viewBox="0 0 8 9"><path d="M1 0.5 L6.5 4.5 L1 8.5" fill="none" stroke="#f06a1a" stroke-width="2"/></svg>mauris ut lectus. Nunc tellus ante, mattis eget, gravida vitae, ultricies ac, leo. Integer leo pede</li>
    </ul>
    <div class="services-photo abs" role="img" aria-label="Open cut coal mine with haul truck on terraced pit"></div>
  </section>

  <div class="divider abs"></div>

  <section class="news">
    <h2 class="section-title abs"><em>ISS</em> News</h2>
    <div class="news-item abs" style="top:863px">
      <div class="news-date">28/02/14</div>
      <p class="body-text">The service offering ranges across contingent permanent recruitment, contract placements, Visa Solutions, managed services and retained search.</p>
    </div>
    <div class="news-sep abs"></div>
    <div class="news-item abs" style="top:937px">
      <div class="news-date">12/02/14</div>
      <p class="body-text">We are guided by 5 key values - collaboration, unity, rigour, accountability and continual improvement. These values unite our team of almost 50, and inspire us to go beyond our expectations</p>
    </div>
    <a class="btn abs" style="left:324px;top:1021px">Read more</a>
  </section>

  <section class="about">
    <h2 class="section-title abs"><em>About</em> ISS</h2>
    <div class="body-text abs">
      <p>We are Karrow Holdings pty ltd trading as Ironvale Shift Services,&nbsp; we are experienced in ground consolidation in underground coal mines,&nbsp; in short when they collapse or cave in we come in with chemical pumps and stabilise the ground or fill cavities which will then allow for the mining process to continue. We also do general mine labor as well.</p>
      <p>We are a labor hire company for major mining services company,&nbsp; we offer labor solutions in New South Wales and Queensland in the underground coal mines. We are a labor hire company for major mining services company,&nbsp; we offer labor solutions in New South Wales and Queensland in the underground coal mines.</p>
    </div>
    <a class="btn abs" style="left:772px;top:1021px">Read more</a>
  </section>

  <footer>
    <div class="footer-band abs">
      <div class="footer-links abs">Home |&nbsp; Apply for position |&nbsp; Pay Portal | Download | Mission | About us | Contact us</div>
      <div class="social abs">
        <i style="background:#3b5a9a"></i><i style="background:#4aa8cf"></i><i style="background:#e8792a"></i><i style="background:#4a8a3a"></i><i style="background:#1a8fd6"></i>
      </div>
    </div>
    <div class="footer-bottom abs">
      <p class="copyright abs">Copy Right © 2014 <b>Ironvale Shift Services.</b> All Rights Reserved</p>
      <div class="payroll-brand abs"><i></i>wagetrakker</div>
    </div>
  </footer>

</div>
</body>
</html>
```